Hitech firm looking for Email header graphics for a new post purchase communication plan

This new communication plan is to get our new customers to feel part of our innovative and hi-tech family. We want to bring professionalism with a cool/fun approach.

We need 3 separate designs for 3 different post purchase email communications:
Email 1: sent immediately after purchase - Welcome & thank you for your order
Email 2: Shipment & tracking notification - Your product has shipped
Email 3: License activation code and instructions - Your license is ready

Our customer service and support team have a 98% customer satisfaction rating, we're good at what we do. For this we wanted to bring those people to life from behind the phone and show our customers who they are actually speaking to. the photos attached are our own employees not stock images, the ones that get rated Awesome, Amazing, life savers and more from existing customers. We want to find a creative way to show they are our guys and they have a sense of humor as well as phenomenal knowledge that saves companies bacon each and every day.

If you can think of a good way to incorporate that in imagery would be great - e.g.names? length of service or a quirky caption e.g. "Backup Wizard Dorian" / "Recovery Viking Hollis" "Ransomware Pirate Osric".

We are open to colour imagery or black/white with a colour pop in red or blue, please see our website www.corvalink.com for our colour style. Our email header template is attached so you can see where the imagery should go.

Also we have created some speech bubbles to include on imagery. feel free to redesign these if you see fit. the wording should not be changed. Colours used are our corporate do not include new colours but feel free to remove the amount of colour if you wish. They do not have to all be used. 6 to choose from.
Updates

Target Market(s)

IT Pros / New customers to Corvalink

Industry/Entity Type

Information Technology

Font styles to use
Sans Serif

Colors

Designer to choose colors to be used in the design.

Requirements
Must have
• 3 separate email header images
Nice to have
• I'd like to see something that identifies these are real Corvalink employees for example: "just a few members of the Corvalink support team" not that exactly I'll leave the creatives to you!
Should not have
• No logo required on this image

```html
<!DOCTYPE html>
<html lang="en">
<head>
<meta charset="utf-8">
<title>Corvalink post-purchase email headers</title>
<link rel="stylesheet" href="https://fonts.googleapis.com/css2?family=Source+Sans+3:wght@400;600&family=Arimo:ital,wght@1,400;1,700&display=swap">
<style>
  :root {
    --page: #ffffff;
    --welcome-red: #e4002b;
    --shipped-blue: #3a69a3;
    --activation-teal: #00b0bb;
    --bubble-blue: #3b5fa7;
    --bubble-teal: #00aeb5;
    --photo-dark: #1a1a1d;
    --photo-mid: #3a3639;
    --prop-orange: #f2771c;
    --prop-red: #d8162b;
    --prop-magenta: #d6249f;
    --prop-yellow: #e9c52a;
    --prop-blue: #2f56b0;
    --prop-lime: #9bd52a;
    --skin-warm: #c98a6a;
    --text-light: #ffffff;
  }
  * { box-sizing: border-box; margin: 0; padding: 0; }
  html, body {
    width: 900px; height: 1200px; overflow: hidden;
    background: var(--page);
  }
  .sheet { position: relative; width: 900px; height: 1200px; }
  .header-banner {
    position: absolute; left: 106px; width: 685px; height: 316px; overflow: hidden;
  }
  .header-banner--welcome { top: 99px; background: var(--welcome-red); }
  .header-banner--shipped { top: 442px; background: var(--shipped-blue); }
  .header-banner--activation { top: 786px; background: var(--activation-teal); }
  .team-photo { position: absolute; inset: 0; width: 685px; height: 316px; }
  .headline {
    position: absolute; left: 0; width: 310px; text-align: center;
    font-family: "Source Sans 3", sans-serif; font-weight: 600;
    font-size: 39px; line-height: 46px; color: var(--text-light);
    letter-spacing: -0.3px;
  }
  .subline {
    position: absolute; left: 0; width: 310px; text-align: center;
    font-family: "Source Sans 3", sans-serif; font-weight: 400;
    font-size: 25px; color: var(--text-light); letter-spacing: -0.2px;
  }
  .header-banner--welcome .headline { top: 78px; }
  .header-banner--welcome .subline { top: 206px; }
  .header-banner--shipped .headline { top: 78px; }
  .header-banner--shipped .subline { top: 205px; }
  .header-banner--activation .headline { top: 78px; }
  .header-banner--activation .subline { top: 207px; }
  .speech-bubble { position: absolute; }
  .speech-bubble svg { position: absolute; inset: 0; }
  .speech-bubble__text {
    position: absolute; left: 0; width: 100%; text-align: center;
    font-family: "Arimo", sans-serif; font-style: italic; font-weight: 700;
    font-size: 14px; line-height: 19px; color: var(--text-light);
  }
  .speech-bubble--zing { left: 504px; top: 88px; width: 130px; height: 110px; }
  .speech-bubble--zing .speech-bubble__text { top: 20px; width: 120px; }
  .speech-bubble--average { left: 422px; top: 170px; width: 125px; height: 110px; }
  .speech-bubble--average .speech-bubble__text { top: 16px; }
  .speech-bubble--superpower { left: 412px; top: 130px; width: 130px; height: 100px; }
  .speech-bubble--superpower .speech-bubble__text { top: 26px; font-size: 12px; line-height: 17px; }
  .speech-bubble--superpower .speech-bubble__text strong { font-size: 14px; }
</style>
</head>
<body>
<main class="sheet">

  <section class="header-banner header-banner--welcome">
    <svg class="team-photo" viewBox="0 0 685 316" role="img" aria-label="Photo area: Corvalink support team members posing in party props – rainbow top hat, masks, crown, polka-dot bow tie and bright feather boas">
      <defs>
        <linearGradient id="base-1" x1="0" y1="0" x2="1" y2="1">
          <stop offset="0" stop-color="var(--photo-mid)"/>
          <stop offset="1" stop-color="var(--photo-dark)"/>
        </linearGradient>
        <radialGradient id="glow-orange-1"><stop offset="0" stop-color="var(--prop-orange)" stop-opacity=".75"/><stop offset="1" stop-color="var(--prop-orange)" stop-opacity="0"/></radialGradient>
        <radialGradient id="glow-red-1"><stop offset="0" stop-color="var(--prop-red)" stop-opacity=".75"/><stop offset="1" stop-color="var(--prop-red)" stop-opacity="0"/></radialGradient>
        <radialGradient id="glow-magenta-1"><stop offset="0" stop-color="var(--prop-magenta)" stop-opacity=".6"/><stop offset="1" stop-color="var(--prop-magenta)" stop-opacity="0"/></radialGradient>
        <radialGradient id="glow-yellow-1"><stop offset="0" stop-color="var(--prop-yellow)" stop-opacity=".55"/><stop offset="1" stop-color="var(--prop-yellow)" stop-opacity="0"/></radialGradient>
        <radialGradient id="glow-blue-1"><stop offset="0" stop-color="var(--prop-blue)" stop-opacity=".5"/><stop offset="1" stop-color="var(--prop-blue)" stop-opacity="0"/></radialGradient>
        <radialGradient id="glow-skin-1"><stop offset="0" stop-color="var(--skin-warm)" stop-opacity=".45"/><stop offset="1" stop-color="var(--skin-warm)" stop-opacity="0"/></radialGradient>
        <clipPath id="photo-clip-1"><polygon points="399,0 685,0 685,316 284,316"/></clipPath>
      </defs>
      <g clip-path="url(#photo-clip-1)">
        <rect width="685" height="316" fill="url(#base-1)"/>
        <ellipse cx="470" cy="120" rx="110" ry="90" fill="url(#glow-skin-1)"/>
        <ellipse cx="630" cy="80" rx="90" ry="80" fill="url(#glow-yellow-1)"/>
        <ellipse cx="540" cy="90" rx="90" ry="60" fill="url(#glow-blue-1)"/>
        <ellipse cx="390" cy="250" rx="110" ry="80" fill="url(#glow-orange-1)"/>
        <ellipse cx="580" cy="270" rx="120" ry="75" fill="url(#glow-red-1)"/>
        <ellipse cx="470" cy="300" rx="80" ry="50" fill="url(#glow-magenta-1)"/>
      </g>
    </svg>
    <h1 class="headline">Welcome<br>To The Circle!!!</h1>
    <p class="subline">are you ready to start?</p>
    <div class="speech-bubble speech-bubble--zing">
      <svg viewBox="0 0 130 110">
        <ellipse cx="60" cy="42" rx="60" ry="42" fill="var(--welcome-red)"/>
        <path d="M82 72 L120 108 L100 66 Z" fill="var(--welcome-red)"/>
      </svg>
      <p class="speech-bubble__text">We Put the<br>ZING<br>in AMAZING!</p>
    </div>
  </section>

  <section class="header-banner header-banner--shipped">
    <svg class="team-photo" viewBox="0 0 685 316" role="img" aria-label="Photo area: Corvalink support team members in wizard hat, pirate hat, mask, sequinned hat and a viking helmet with orange beard">
      <defs>
        <linearGradient id="base-2" x1="0" y1="0" x2="1" y2="1">
          <stop offset="0" stop-color="var(--photo-mid)"/>
          <stop offset="1" stop-color="var(--photo-dark)"/>
        </linearGradient>
        <radialGradient id="glow-orange-2"><stop offset="0" stop-color="var(--prop-orange)" stop-opacity=".8"/><stop offset="1" stop-color="var(--prop-orange)" stop-opacity="0"/></radialGradient>
        <radialGradient id="glow-blue-2"><stop offset="0" stop-color="var(--prop-blue)" stop-opacity=".6"/><stop offset="1" stop-color="var(--prop-blue)" stop-opacity="0"/></radialGradient>
        <radialGradient id="glow-yellow-2"><stop offset="0" stop-color="var(--prop-yellow)" stop-opacity=".5"/><stop offset="1" stop-color="var(--prop-yellow)" stop-opacity="0"/></radialGradient>
        <radialGradient id="glow-magenta-2"><stop offset="0" stop-color="var(--prop-magenta)" stop-opacity=".5"/><stop offset="1" stop-color="var(--prop-magenta)" stop-opacity="0"/></radialGradient>
        <radialGradient id="glow-skin-2"><stop offset="0" stop-color="var(--skin-warm)" stop-opacity=".45"/><stop offset="1" stop-color="var(--skin-warm)" stop-opacity="0"/></radialGradient>
        <clipPath id="photo-clip-2"><polygon points="399,0 685,0 685,316 284,316"/></clipPath>
      </defs>
      <g clip-path="url(#photo-clip-2)">
        <rect width="685" height="316" fill="url(#base-2)"/>
        <ellipse cx="500" cy="150" rx="130" ry="90" fill="url(#glow-skin-2)"/>
        <ellipse cx="490" cy="110" rx="70" ry="40" fill="url(#glow-blue-2)"/>
        <ellipse cx="400" cy="160" rx="70" ry="50" fill="url(#glow-yellow-2)"/>
        <ellipse cx="620" cy="200" rx="70" ry="90" fill="url(#glow-orange-2)"/>
        <ellipse cx="650" cy="40" rx="60" ry="40" fill="url(#glow-magenta-2)"/>
      </g>
    </svg>
    <h2 class="headline">Your Product<br>Has Shipped!!!</h2>
    <p class="subline">let the good times roll...</p>
    <div class="speech-bubble speech-bubble--average">
      <svg viewBox="0 0 125 110">
        <ellipse cx="62" cy="42" rx="62" ry="42" fill="var(--bubble-blue)"/>
        <path d="M80 74 L88 108 L104 68 Z" fill="var(--bubble-blue)"/>
      </svg>
      <p class="speech-bubble__text">I Don’t Do<br>Average, I do<br>AWESOME!</p>
    </div>
  </section>

  <section class="header-banner header-banner--activation">
    <svg class="team-photo" viewBox="0 0 685 316" role="img" aria-label="Photo area: Corvalink support team members in sombrero, crowns, sun hats, novelty glasses and colourful feather boas">
      <defs>
        <linearGradient id="base-3" x1="0" y1="0" x2="1" y2="1">
          <stop offset="0" stop-color="var(--photo-mid)"/>
          <stop offset="1" stop-color="var(--photo-dark)"/>
        </linearGradient>
        <radialGradient id="glow-yellow-3"><stop offset="0" stop-color="var(--prop-yellow)" stop-opacity=".55"/><stop offset="1" stop-color="var(--prop-yellow)" stop-opacity="0"/></radialGradient>
        <radialGradient id="glow-magenta-3"><stop offset="0" stop-color="var(--prop-magenta)" stop-opacity=".75"/><stop offset="1" stop-color="var(--prop-magenta)" stop-opacity="0"/></radialGradient>
        <radialGradient id="glow-red-3"><stop offset="0" stop-color="var(--prop-red)" stop-opacity=".6"/><stop offset="1" stop-color="var(--prop-red)" stop-opacity="0"/></radialGradient>
        <radialGradient id="glow-lime-3"><stop offset="0" stop-color="var(--prop-lime)" stop-opacity=".6"/><stop offset="1" stop-color="var(--prop-lime)" stop-opacity="0"/></radialGradient>
        <radialGradient id="glow-orange-3"><stop offset="0" stop-color="var(--prop-orange)" stop-opacity=".6"/><stop offset="1" stop-color="var(--prop-orange)" stop-opacity="0"/></radialGradient>
        <radialGradient id="glow-skin-3"><stop offset="0" stop-color="var(--skin-warm)" stop-opacity=".45"/><stop offset="1" stop-color="var(--skin-warm)" stop-opacity="0"/></radialGradient>
        <clipPath id="photo-clip-3"><polygon points="399,0 685,0 685,316 284,316"/></clipPath>
      </defs>
      <g clip-path="url(#photo-clip-3)">
        <rect width="685" height="316" fill="url(#base-3)"/>
        <ellipse cx="480" cy="50" rx="110" ry="50" fill="url(#glow-yellow-3)"/>
        <ellipse cx="520" cy="140" rx="130" ry="80" fill="url(#glow-skin-3)"/>
        <ellipse cx="440" cy="130" rx="60" ry="60" fill="url(#glow-red-3)"/>
        <ellipse cx="560" cy="170" rx="70" ry="80" fill="url(#glow-magenta-3)"/>
        <ellipse cx="540" cy="270" rx="40" ry="60" fill="url(#glow-lime-3)"/>
        <ellipse cx="650" cy="260" rx="60" ry="50" fill="url(#glow-orange-3)"/>
        <ellipse cx="640" cy="170" rx="60" ry="50" fill="url(#glow-yellow-3)"/>
      </g>
    </svg>
    <h2 class="headline">Your Activation<br>Is Here!!!</h2>
    <p class="subline">you’re good to go...</p>
    <div class="speech-bubble speech-bubble--superpower">
      <svg viewBox="0 0 130 100">
        <ellipse cx="65" cy="56" rx="62" ry="42" fill="var(--bubble-teal)"/>
        <path d="M10 4 L42 22 L26 30 Z" fill="var(--bubble-teal)"/>
      </svg>
      <p class="speech-bubble__text">Delighting<br>customers is my<br><strong>SUPERPOWER</strong></p>
    </div>
  </section>

</main>
</body>
</html>
```